Business Card Design Project

Create an impressive business care to use
Updates

My logo is available at http://corvalune.example, or

Industry/Entity Type

Business

Requirements
Must have
• company logo

```html
<!DOCTYPE html>
<html lang="en">
<head>
<meta charset="utf-8">
<title>Corvalune Research Corporation – Business Card</title>
<link rel="stylesheet" href="https://fonts.googleapis.com/css2?family=Montserrat:wght@500&family=Open+Sans:wght@400;700&display=swap">
<style>
  :root {
    --card-light: #fbfbfb;
    --card-mid: #ececec;
    --card-shade: #d9d9d9;
    --sweep: #ffffff;
    --ink: #3b3b3d;
    --brand-ink: #3d3d40;
    --accent-green: #8dbb3f;
    --accent-blue: #1ba3e0;
    --accent-orange: #f6a43a;
  }
  * { margin: 0; padding: 0; box-sizing: border-box; }
  html, body {
    width: 1200px;
    height: 600px;
    overflow: hidden;
    background: #ffffff;
  }
  .business-card {
    position: relative;
    width: 1200px;
    height: 600px;
    overflow: hidden;
    background: linear-gradient(160deg, var(--card-light) 0%, var(--card-mid) 55%, var(--card-shade) 100%);
    font-family: "Open Sans", Arial, sans-serif;
    color: var(--ink);
  }
  .card-backdrop {
    position: absolute;
    inset: 0;
    width: 1200px;
    height: 600px;
  }
  .accent-artwork {
    position: absolute;
  }
  .accent-artwork--top {
    left: 864px;
    top: 0;
    width: 336px;
    height: 200px;
  }
  .accent-artwork--bottom {
    left: 846px;
    top: 472px;
    width: 354px;
    height: 128px;
  }
  .brand-lockup {
    position: absolute;
    left: 58px;
    top: 36px;
    color: var(--brand-ink);
    font-family: "Montserrat", Arial, sans-serif;
    font-weight: 500;
  }
  .brand-name {
    font-size: 70px;
    letter-spacing: 8px;
    line-height: 1;
  }
  .brand-tagline {
    margin-top: 12px;
    font-size: 21px;
    letter-spacing: 7.4px;
    line-height: 1;
  }
  .contact-block {
    position: absolute;
    left: 38px;
    top: 378px;
  }
  .company-name,
  .contact-label {
    font-weight: 700;
    font-size: 27px;
    line-height: 38px;
  }
  .company-address,
  .contact-email {
    font-weight: 400;
    font-size: 27px;
    line-height: 38px;
  }
  .contact-label { margin-top: 34px; }
  .contact-email a { color: inherit; text-decoration: none; }
</style>
</head>
<body>
  <main class="business-card">
    <svg class="card-backdrop" viewBox="0 0 1200 600" aria-hidden="true">
      <path class="light-sweep" d="M0,0 H330 C520,260 820,470 1200,545 V600 H0 Z" fill="var(--sweep)" opacity="0.55"/>
      <path class="light-sweep-edge" d="M330,0 C520,260 820,470 1200,545" fill="none" stroke="var(--sweep)" stroke-width="3" opacity="0.9"/>
    </svg>

    <svg class="accent-artwork accent-artwork--top" viewBox="0 0 336 200" role="img" aria-label="Decorative artwork in green, blue and orange at the top right corner">
      <defs>
        <linearGradient id="top-artwork-tone" x1="0" y1="0" x2="1" y2="1">
          <stop offset="0" stop-color="var(--accent-green)" stop-opacity="0.55"/>
          <stop offset="0.5" stop-color="var(--accent-blue)" stop-opacity="0.45"/>
          <stop offset="1" stop-color="var(--accent-orange)" stop-opacity="0.55"/>
        </linearGradient>
      </defs>
      <rect width="336" height="200" fill="url(#top-artwork-tone)"/>
    </svg>

    <svg class="accent-artwork accent-artwork--bottom" viewBox="0 0 354 128" role="img" aria-label="Decorative stripe pattern in green, blue and orange at the bottom right corner">
      <defs>
        <linearGradient id="bottom-artwork-tone" x1="0" y1="1" x2="1" y2="0">
          <stop offset="0" stop-color="var(--accent-green)" stop-opacity="0.6"/>
          <stop offset="0.5" stop-color="var(--accent-orange)" stop-opacity="0.5"/>
          <stop offset="1" stop-color="var(--accent-blue)" stop-opacity="0.6"/>
        </linearGradient>
      </defs>
      <rect width="354" height="128" fill="url(#bottom-artwork-tone)"/>
    </svg>

    <header class="brand-lockup">
      <p class="brand-name">CORVALUNE</p>
      <p class="brand-tagline">RESEARCH CORPORATION</p>
    </header>

    <section class="contact-block">
      <p class="company-name">Corvalune Research Corporation</p>
      <p class="company-address">2740 Harbor Ridge Way, Suite 210, Fairmont, CA 90417</p>
      <p class="contact-label">Email:</p>
      <p class="contact-email"><a href="mailto:PublicRelations@corvalune.example">PublicRelations@corvalune.example</a></p>
    </section>
  </main>
</body>
</html>
```